Finiding oppertunites in Real Estate 6.15.20

size of ad 7” x 9.6”
1-I like the ad to stand out and attract people's attention.
2-you should be able to see the text of the ad clearly .. see the attachment anything in yellow is instructions.
3-the list of topics should not be the main part of the ad
4-if you decide you want a picture or vector of a person .. (you decide)
then it should be a white male about 25-30 years old wearing a solid white or blue shirt and not long hair.
5-leave 1 inch for footer
see attachment
Good luck

Target Market(s)

potential male students 25-35 years of age

Industry/Entity Type

Education

Requirements
Must have
• will stand out and people would want to see it.
should be able to read the words of ad
Nice to have
• how to make money in real estate on one line

```html
<!DOCTYPE html>
<html lang="en">
<head>
<meta charset="utf-8">
<title>Real Estate Career Course Flyer</title>
<link href="https://fonts.googleapis.com/css2?family=Montserrat:wght@300;400;500;600;700;800;900&family=Roboto+Condensed:wght@700&display=swap" rel="stylesheet">
<style>
  :root {
    --stage: #5d574a;
    --paper: #ffffff;
    --gold: #b69855;
    --gold-light: #d9c596;
    --gold-soft: #e8dcc0;
    --navy: #23487a;
    --red: #e01b24;
    --ink: #2a2a2a;
    --footer: #efefef;
  }
  * { box-sizing: border-box; margin: 0; padding: 0; }
  html, body { width: 1200px; height: 1191px; overflow: hidden; }
  body {
    background: var(--stage);
    font-family: "Montserrat", Arial, sans-serif;
    position: relative;
  }
  .flyer {
    position: absolute;
    left: 190px; top: 33px;
    width: 820px; height: 1124px;
    background: linear-gradient(180deg, var(--paper) 0%, var(--paper) 52%, #f4eee0 66%, var(--gold-soft) 89%, var(--paper) 89.6%);
    overflow: hidden;
  }
  .title {
    position: absolute; top: 50px; left: 0; width: 100%;
    text-align: center; color: var(--gold);
    font-weight: 900; font-size: 64px; line-height: 66px; letter-spacing: 1px;
  }
  .band {
    position: absolute; left: 50%; transform: translateX(-50%);
    background: var(--navy); color: #fff; text-align: center;
    font-weight: 600; box-shadow: 4px 5px 6px rgba(0,0,0,.25);
  }
  .band--question { top: 198px; width: 600px; padding: 9px 0; font-size: 29px; line-height: 34px; }
  .band--audience { top: 264px; width: 620px; padding: 8px 0; font-size: 28px; line-height: 34px; }
  .tagline {
    position: absolute; top: 362px; left: 0; width: 100%;
    text-align: center; color: var(--red);
    font-weight: 800; font-size: 40px; line-height: 46px;
  }
  .houses {
    position: absolute; top: 462px; left: 70px; width: 690px; height: 150px;
    background: radial-gradient(ellipse at 50% 55%, #e4e4e4 0%, #f3f3f3 45%, rgba(255,255,255,0) 72%);
  }
  .houses .accent {
    position: absolute; left: 330px; top: 78px; width: 44px; height: 44px;
    background: #d7252a; border-radius: 4px;
  }
  .promo {
    position: absolute; top: 620px; left: 70px; width: 690px; height: 180px;
    background: linear-gradient(90deg, var(--gold) 0%, var(--gold-light) 48%, var(--gold-light) 52%, var(--gold) 100%);
  }
  .promo__divider {
    position: absolute; left: 320px; top: 18px; width: 2px; height: 144px; background: #fff;
  }
  .remote__art {
    position: absolute; left: 36px; top: 10px; width: 190px; height: 80px;
    background: linear-gradient(135deg, #f0a43a, #3e6fa8); border-radius: 4px; opacity: .85;
  }
  .remote__label {
    position: absolute; left: 30px; top: 82px; color: #fff;
    font-weight: 300; font-size: 46px; line-height: 46px; letter-spacing: 1px;
  }
  .course__count {
    position: absolute; left: 360px; top: 10px; width: 300px; text-align: center;
    color: #fff; font-weight: 400; font-size: 42px; line-height: 40px;
  }
  .course__start {
    position: absolute; left: 350px; top: 94px; width: 315px; padding: 6px 0;
    background: #fff; text-align: center; color: var(--navy);
    font-size: 30px; line-height: 32px; font-weight: 400;
  }
  .course__start strong { font-weight: 800; }
  .topics__heading {
    position: absolute; top: 812px; left: 0; width: 100%; text-align: center;
    color: var(--navy); font-weight: 700; font-size: 21px; line-height: 28px;
  }
  .topics {
    position: absolute; top: 850px; left: 90px; width: 660px;
    display: flex; justify-content: space-between;
  }
  .topics ul { list-style: none; }
  .topics li {
    display: flex; align-items: center; gap: 10px;
    font-size: 14.5px; color: var(--ink); line-height: 25px; font-weight: 500;
  }
  .tick { width: 13px; height: 13px; flex: none; }
  .footer {
    position: absolute; left: 0; bottom: 0; width: 100%; height: 117px;
    background: var(--footer);
    display: flex; align-items: center; justify-content: space-between; padding: 0 44px;
  }
  .contact-line {
    display: flex; align-items: center; gap: 10px;
    font-size: 14px; color: var(--ink); line-height: 22px;
  }
  .contact-line svg { width: 16px; height: 16px; flex: none; }
  .address .contact-line svg { width: 22px; height: 30px; }
  .hotline { text-align: right; }
  .hotline__label { color: var(--red); font-weight: 900; font-size: 34px; line-height: 34px; }
  .hotline__number { font-family: "Roboto Condensed", Arial, sans-serif; font-weight: 700; font-size: 20px; color: #111; }
</style>
</head>
<body>
<main class="flyer">
  <h1 class="title">REAL ESTATE<br>CAREER COURSE</h1>
  <p class="band band--question">How to Make Money In Real Estate?</p>
  <p class="band band--audience">For those who have started or<br>would like to go into Real Estate.</p>
  <p class="tagline">An investment in knowledge<br>opens up untold opportunities.</p>

  <div class="houses" role="img" aria-label="Field of small white model houses with one red house standing out">
    <span class="accent"></span>
  </div>

  <section class="promo">
    <div class="remote__art" role="img" aria-label="Illustration of a young man at a laptop joining a remote real estate session"></div>
    <p class="remote__label">REMOTE<br>SESSIONS</p>
    <span class="promo__divider"></span>
    <p class="course__count">12 session<br>course</p>
    <p class="course__start">Classes starting<br><strong>June 16</strong></p>
  </section>

  <h2 class="topics__heading">A partial listing of Topics</h2>
  <div class="topics">
    <ul>
      <li><svg class="tick" viewBox="0 0 13 13"><rect x=".5" y=".5" width="12" height="12" fill="none" stroke="#b69855"/><path d="M3 6.5l2.5 2.5L11 2" fill="none" stroke="#b69855" stroke-width="1.4"/></svg>Single-family</li>
      <li><svg class="tick" viewBox="0 0 13 13"><rect x=".5" y=".5" width="12" height="12" fill="none" stroke="#b69855"/><path d="M3 6.5l2.5 2.5L11 2" fill="none" stroke="#b69855" stroke-width="1.4"/></svg>Multifamily</li>
      <li><svg class="tick" viewBox="0 0 13 13"><rect x=".5" y=".5" width="12" height="12" fill="none" stroke="#b69855"/><path d="M3 6.5l2.5 2.5L11 2" fill="none" stroke="#b69855" stroke-width="1.4"/></svg>Management</li>
      <li><svg class="tick" viewBox="0 0 13 13"><rect x=".5" y=".5" width="12" height="12" fill="none" stroke="#b69855"/><path d="M3 6.5l2.5 2.5L11 2" fill="none" stroke="#b69855" stroke-width="1.4"/></svg>Real Estate Concepts</li>
      <li><svg class="tick" viewBox="0 0 13 13"><rect x=".5" y=".5" width="12" height="12" fill="none" stroke="#b69855"/><path d="M3 6.5l2.5 2.5L11 2" fill="none" stroke="#b69855" stroke-width="1.4"/></svg>Real Estate law</li>
    </ul>
    <ul>
      <li><svg class="tick" viewBox="0 0 13 13"><rect x=".5" y=".5" width="12" height="12" fill="none" stroke="#b69855"/><path d="M3 6.5l2.5 2.5L11 2" fill="none" stroke="#b69855" stroke-width="1.4"/></svg>Investment properties</li>
      <li><svg class="tick" viewBox="0 0 13 13"><rect x=".5" y=".5" width="12" height="12" fill="none" stroke="#b69855"/><path d="M3 6.5l2.5 2.5L11 2" fill="none" stroke="#b69855" stroke-width="1.4"/></svg>Foreclosures</li>
      <li><svg class="tick" viewBox="0 0 13 13"><rect x=".5" y=".5" width="12" height="12" fill="none" stroke="#b69855"/><path d="M3 6.5l2.5 2.5L11 2" fill="none" stroke="#b69855" stroke-width="1.4"/></svg>Rehab</li>
      <li><svg class="tick" viewBox="0 0 13 13"><rect x=".5" y=".5" width="12" height="12" fill="none" stroke="#b69855"/><path d="M3 6.5l2.5 2.5L11 2" fill="none" stroke="#b69855" stroke-width="1.4"/></svg>Foreclosures</li>
      <li><svg class="tick" viewBox="0 0 13 13"><rect x=".5" y=".5" width="12" height="12" fill="none" stroke="#b69855"/><path d="M3 6.5l2.5 2.5L11 2" fill="none" stroke="#b69855" stroke-width="1.4"/></svg>Short sales</li>
    </ul>
    <ul>
      <li><svg class="tick" viewBox="0 0 13 13"><rect x=".5" y=".5" width="12" height="12" fill="none" stroke="#b69855"/><path d="M3 6.5l2.5 2.5L11 2" fill="none" stroke="#b69855" stroke-width="1.4"/></svg>Development</li>
      <li><svg class="tick" viewBox="0 0 13 13"><rect x=".5" y=".5" width="12" height="12" fill="none" stroke="#b69855"/><path d="M3 6.5l2.5 2.5L11 2" fill="none" stroke="#b69855" stroke-width="1.4"/></svg>Finical modeling</li>
      <li><svg class="tick" viewBox="0 0 13 13"><rect x=".5" y=".5" width="12" height="12" fill="none" stroke="#b69855"/><path d="M3 6.5l2.5 2.5L11 2" fill="none" stroke="#b69855" stroke-width="1.4"/></svg>HUD properties</li>
      <li><svg class="tick" viewBox="0 0 13 13"><rect x=".5" y=".5" width="12" height="12" fill="none" stroke="#b69855"/><path d="M3 6.5l2.5 2.5L11 2" fill="none" stroke="#b69855" stroke-width="1.4"/></svg>Due Diligence</li>
    </ul>
  </div>

  <footer class="footer">
    <div class="address">
      <p class="contact-line">
        <svg viewBox="0 0 22 30"><path d="M11 1a9 9 0 0 0-9 9c0 7 9 18 9 18s9-11 9-18a9 9 0 0 0-9-9z" fill="#b69855"/><circle cx="11" cy="10" r="4" fill="#fff"/></svg>
        <span>ur address goes here,<br>street Crossroad 123</span>
      </p>
    </div>
    <div class="contacts">
      <p class="contact-line"><svg viewBox="0 0 16 16"><path d="M3 1l3 3-2 2c1 2 3 4 6 6l2-2 3 3-2 2C7 15 1 9 1 3z" fill="#b69855"/></svg>+012 - 3456 - 78901</p>
      <p class="contact-line"><svg viewBox="0 0 16 16"><rect x="1" y="3" width="14" height="10" fill="#b69855"/><path d="M1 3l7 6 7-6" fill="none" stroke="#fff" stroke-width="1.3"/></svg>urname@email.com</p>
      <p class="contact-line"><svg viewBox="0 0 16 16"><circle cx="8" cy="8" r="7" fill="#b69855"/><path d="M1 8h14M8 1c-3 4-3 10 0 14M8 1c3 4 3 10 0 14" fill="none" stroke="#fff" stroke-width="1"/></svg>urwebsitename.com</p>
    </div>
    <div class="hotline">
      <p class="hotline__label">HOTLINE</p>
      <p class="hotline__number">+012 - 3456 - 78901</p>
    </div>
  </footer>
</main>
</body>
</html>
```